Baby Shower Invitation for Vectored Image Provided

Caroline & Desmond's Baby Shower - Black/White/Gold Colors preferred
Please use the vectored portrait image attached. I'd like us on the lower right side of the invitation.
Can be horizontal or vertical layout.
The second image attached has the information needed for you to complete.
I don't want that style copied, it is just an example.

```html
<!DOCTYPE html>
<html lang="en">
<head>
<meta charset="utf-8">
<title>Baby Shower Invitation</title>
<link rel="stylesheet" href="https://fonts.googleapis.com/css2?family=Dancing+Script:wght@500;600&family=Vollkorn:wght@400;500&display=swap">
<style>
  :root {
    --bg-dark: #1c1c1c;
    --bg-mid: #2e2e2e;
    --ink: #f4f1ea;
    --gold: #e9c45a;
    --gold-light: #f6dc86;
    --gold-deep: #c99a2e;
    --rule: #c9a448;
    --portrait-a: #4a4a4a;
    --portrait-b: #141414;
  }
  * { margin: 0; padding: 0; box-sizing: border-box; }
  html, body { width: 857px; height: 1200px; overflow: hidden; background: var(--bg-dark); }
  .invitation {
    position: relative;
    width: 857px;
    height: 1200px;
    overflow: hidden;
    background: radial-gradient(ellipse at 50% 45%, var(--bg-mid) 0%, var(--bg-dark) 78%);
    color: var(--ink);
    font-family: "Vollkorn", Georgia, serif;
    font-variant-numeric: oldstyle-nums;
  }
  .stars { position: absolute; inset: 0; width: 857px; height: 1200px; }
  .line {
    position: absolute;
    white-space: nowrap;
    text-align: center;
    transform: translate(-50%, -50%);
  }
  .caps { font-size: 18px; letter-spacing: 0.28em; font-weight: 500; }
  .eyebrow { top: 152px; left: 429px; }
  .tagline { top: 324px; left: 425px; letter-spacing: 0.3em; }
  .script {
    font-family: "Dancing Script", "Brush Script MT", cursive;
    color: var(--gold);
    font-weight: 600;
    font-style: normal;
  }
  .headline { top: 236px; left: 428px; font-size: 76px; }
  .lead { top: 430px; left: 425px; font-size: 21px; letter-spacing: 0.07em; font-weight: 500; }
  .honoree { top: 520px; left: 432px; font-size: 84px; }
  .detail { font-size: 26px; }
  .when { top: 618px; left: 433px; }
  .where { top: 672px; left: 433px; }
  .rsvp { top: 804px; left: 288px; }
  .rsvp-2 { top: 844px; left: 288px; }
  .registry { top: 954px; left: 288px; }
  .registry-2 { top: 994px; left: 288px; }
  .signoff { top: 1094px; left: 288px; font-size: 54px; }
  .rule { position: absolute; height: 3px; background: var(--rule); }
  .rule-top { left: 326px; top: 376px; width: 209px; }
  .rule-mid { left: 181px; top: 748px; width: 208px; }
  .rule-low { left: 181px; top: 902px; width: 208px; }
  .portrait {
    position: absolute;
    left: 522px;
    top: 744px;
    width: 328px;
    height: 456px;
    border-radius: 120px 120px 0 0;
    background: linear-gradient(180deg, var(--portrait-a) 0%, var(--portrait-b) 100%);
  }
</style>
</head>
<body>
<main class="invitation">
  <svg class="stars" viewBox="0 0 857 1200" aria-hidden="true">
    <defs>
      <linearGradient id="star-fill" x1="0" y1="0" x2="1" y2="1">
        <stop offset="0" stop-color="#f6dc86"/>
        <stop offset="1" stop-color="#c99a2e"/>
      </linearGradient>
      <polygon id="star" points="0,-16 4.7,-5.2 16,-4.9 7.4,2.4 10.2,13.6 0,7.2 -10.2,13.6 -7.4,2.4 -16,-4.9 -4.7,-5.2" fill="url(#star-fill)"/>
    </defs>
    <use href="#star" x="24" y="8"/>
    <use href="#star" x="228" y="8"/>
    <use href="#star" x="360" y="8"/>
    <use href="#star" x="484" y="8"/>
    <use href="#star" x="624" y="8"/>
    <use href="#star" x="748" y="8"/>
    <use href="#star" x="844" y="60"/>
    <use href="#star" x="120" y="60"/>
    <use href="#star" x="284" y="84"/>
    <use href="#star" x="396" y="86"/>
    <use href="#star" x="552" y="84"/>
    <use href="#star" x="660" y="86"/>
    <use href="#star" x="22" y="108"/>
    <use href="#star" x="138" y="132"/>
    <use href="#star" x="766" y="124"/>
    <use href="#star" x="50" y="198"/>
    <use href="#star" x="816" y="198"/>
    <use href="#star" x="56" y="1044"/>
    <use href="#star" x="8" y="1116"/>
    <use href="#star" x="156" y="1164"/>
    <use href="#star" x="428" y="1164"/>
    <use href="#star" x="48" y="1188"/>
    <use href="#star" x="500" y="1044"/>
  </svg>

  <p class="line caps eyebrow">TWINKLE, TWINKLE</p>
  <h1 class="line script headline">little boy</h1>
  <p class="line caps tagline">DO YOU KNOW HOW LOVED YOU ARE?</p>
  <div class="rule rule-top"></div>

  <p class="line lead">Please join us for a baby shower honoring</p>
  <h2 class="line script honoree">Caroline Hollowell</h2>
  <p class="line detail when">Saturday, September 1st, 11:30am-2:30pm</p>
  <p class="line detail where">The Willowmere 4180 Ashford Ln. Raleigh, NC</p>

  <div class="rule rule-mid"></div>
  <p class="line detail rsvp">RSVP to Desmond at</p>
  <p class="line detail rsvp-2">919-555-0148 by August 20th</p>

  <div class="rule rule-low"></div>
  <p class="line detail registry">Caroline is registered at</p>
  <p class="line detail registry-2">Little Nest Baby</p>

  <p class="line script signoff">See You There!</p>

  <div class="portrait" role="img" aria-label="Vector portrait of the expecting couple, the man standing behind the pregnant woman with his hands on her belly"></div>
</main>
</body>
</html>
```